I'm looking for a movie poster for my short film, "The Shelf Tailor."

Requirements
Must have
• HOLLOW LANTERN PRODUCTIONS presents a film written and directed by CLARA VOSTRIKOVA starring OWEN TRELAWNEY, GREGORY PALTRO and MARNABELL QUORSTAD "THE SHELF TAILOR" 1st assistant director HELGA TRIMBLE director of photography TAVOREN FLINT edited by OSKAR LUM executive producers PAM & HUGO STERNFIELD produced by MATTIAS KORVELL and CLARA VOSTRIKOVA

```html
<!DOCTYPE html>
<html lang="en">
<head>
<meta charset="utf-8">
<title>The Shelf Tailor — Poster</title>
<link rel="stylesheet" href="https://fonts.googleapis.com/css2?family=Josefin+Sans:wght@400;600&family=Archivo+Narrow:wght@500;600&family=Libre+Baskerville:ital,wght@1,700&display=swap">
<style>
  :root {
    --page-bg: #2a2a2a;
    --ink-white: #ffffff;
    --ink-gold: #e6c25a;
    --bar-warm-1: #c9a27c;
    --bar-warm-2: #8a4b33;
    --bar-dark: #2b1a14;
    --shelf-1: #3a3a2a;
    --shelf-2: #1d1b1f;
    --shelf-3: #0f0e12;
  }
  * { margin: 0; padding: 0; box-sizing: border-box; }
  html, body { width: 1200px; height: 900px; overflow: hidden; background: var(--page-bg); }
  .poster {
    position: absolute; left: 290px; top: 20px; width: 620px; height: 860px;
    overflow: hidden; color: var(--ink-white);
    font-family: "Archivo Narrow", "Arial Narrow", sans-serif;
  }
  .poster__scene-bar {
    position: absolute; left: 0; top: 0; width: 100%; height: 430px;
    background:
      linear-gradient(180deg, rgba(20,14,12,.85) 0%, rgba(20,14,12,0) 22%),
      linear-gradient(90deg, var(--bar-warm-1) 0%, var(--bar-warm-2) 45%, #b5653f 70%, var(--bar-dark) 100%);
  }
  .poster__scene-shelves {
    position: absolute; left: 0; top: 390px; width: 100%; height: 470px;
    background:
      linear-gradient(180deg, rgba(0,0,0,0) 0%, rgba(0,0,0,.35) 100%),
      linear-gradient(90deg, var(--shelf-1) 0%, var(--shelf-2) 40%, #3a2c34 70%, var(--shelf-3) 100%);
  }
  .poster__scene-shelves::before {
    content: ""; position: absolute; inset: 0 0 auto 0; height: 60px;
    background: linear-gradient(180deg, #6b4a36 0%, rgba(107,74,54,0) 100%);
  }
  .cast {
    position: absolute; right: 34px; top: 30px; text-align: right;
    font-weight: 600; font-size: 19px; line-height: 1.12; letter-spacing: .5px;
  }
  .title {
    position: absolute; left: 0; right: 0; top: 345px; text-align: center;
    font-family: "Josefin Sans", sans-serif; font-weight: 400;
    font-size: 86px; line-height: 1.22; letter-spacing: 2px;
  }
  .presents {
    position: absolute; left: 0; right: 0; top: 638px; text-align: center;
    font-weight: 600; font-size: 14px; line-height: 1.05;
  }
  .tagline {
    position: absolute; left: 0; right: 0; top: 702px; text-align: center;
    font-family: "Libre Baskerville", serif; font-style: italic; font-weight: 700;
    font-size: 15px; color: var(--ink-gold);
  }
  .crew { position: absolute; top: 726px; font-weight: 500; font-size: 15px; line-height: 1.08; }
  .crew--left { left: 30px; }
  .crew--right { right: 30px; top: 738px; text-align: right; }
  .crew__name { font-weight: 600; }
</style>
</head>
<body>
  <main class="poster">
    <div class="poster__scene-bar" role="img" aria-label="Photo of a pub interior with bar counter, dartboards and a man seated at a table"></div>
    <div class="poster__scene-shelves" role="img" aria-label="Blurred photo of shelves filled with boxed sets"></div>

    <p class="cast">STARRING<br>OWEN TRELAWNEY<br>GREGORY PALTRO AND<br>MARNABELL QUORSTAD</p>

    <h1 class="title">THE SHELF<br>TAILOR</h1>

    <p class="presents">HOLLOW LANTERN PRODUCTIONS PRESENTS<br>A FILM WRITTEN AND DIRECTED<br>BY<br>CLARA VOSTRIKOVA</p>

    <p class="tagline">Friends don't let friends fly solo.</p>

    <p class="crew crew--left">1ST ASSISTANT DIRECTOR<br><span class="crew__name">HELGA TRIMBLE</span><br>DIRECTOR OF PHOTOGRAPHY<br><span class="crew__name">TAVOREN FLINT</span><br>EDITED BY OSKAR LUM</p>

    <p class="crew crew--right">EXECUTIVE PRODUCERS<br><span class="crew__name">PAM &amp; HUGO STERNFIELD</span><br>PRODUCED BY<br><span class="crew__name">MATTIAS KORVELL AND<br>CLARA VOSTRIKOVA</span></p>
  </main>
</body>
</html>
```